menu board design: harbor burger

we are a burger restaurant.
we need to re design our menu board to fit within the new design of the restaurant. we are after something simple and easy to read. the overall look and feel of the design should be inline with the design of the shop.

Target Market(s)

18-40 male and female

Colors

Designer to choose colors to be used in the design.

Requirements
Must have
• easy to read. good layout. white background. branding included in design.

```html
<!DOCTYPE html>
<html lang="en">
<head>
<meta charset="utf-8">
<title>Harbor Burger Menu Board</title>
<link href="https://fonts.googleapis.com/css2?family=Bangers&family=Nunito:wght@400;600;700;800&display=swap" rel="stylesheet">
<style>
:root{
  --board:#1f4a5c;
  --yellow:#e8b923;
  --ink-blue:#1c3f9e;
  --ink-red:#c22a2b;
  --white:#ffffff;
  --chalk:#eef2f4;
}
*{margin:0;padding:0;box-sizing:border-box}
html,body{width:1200px;height:600px;overflow:hidden;background:var(--board)}
.board{position:relative;width:1200px;height:600px;background:var(--board);color:var(--white);font-family:'Nunito',sans-serif}
.abs{position:absolute}
.band{position:absolute;background:var(--yellow);display:flex;align-items:center;justify-content:center;font-family:'Bangers',sans-serif;color:var(--ink-blue);letter-spacing:1px}
.band--red{color:var(--ink-red)}
.intro{font-size:11px;line-height:14.5px;text-align:center}
.note{font-size:11px;font-weight:700;color:var(--yellow);text-align:center;letter-spacing:.3px}
.item{position:absolute;width:313px}
.item__row{display:flex;align-items:baseline;color:var(--yellow);font-weight:700;font-size:11.5px;letter-spacing:.3px}
.item__dots{flex:1;border-bottom:1.5px dotted var(--yellow);margin:0 2px;transform:translateY(-3px)}
.item__desc{font-size:9.6px;line-height:13px;text-align:justify;margin-top:2px}
.rule{position:absolute;height:2px;background:var(--chalk);opacity:.9}
.brand{position:absolute;left:386px;top:29px;width:420px;height:298px;border-radius:50%;background:var(--white);text-align:center}
.brand__name{position:absolute;left:0;right:0;top:92px;font-family:'Nunito',sans-serif;font-weight:800;font-size:50px;line-height:56px;color:var(--ink-blue)}
.brand__tag{position:absolute;left:0;right:0;top:243px;font-size:11.5px;letter-spacing:5px;color:var(--ink-blue);font-weight:600}
.sides{position:absolute;left:482px;width:220px}
.sides .item__row{font-size:15px}
.sides__desc{font-size:10.3px;line-height:13px}
.art{position:absolute;background:linear-gradient(#2a5a6e,#24505f);border-radius:8px;border:1px solid rgba(255,255,255,.35)}
.ornament{position:absolute;width:22px;height:22px;border-radius:50%;background:rgba(238,242,244,.75)}
.step-label{font-size:11px;font-weight:700;text-align:center}
.choice{font-size:11px;font-weight:700}
.choice .item__dots{border-color:var(--white)}
.price-w{font-weight:400}
.nachos-desc{font-size:10.3px;line-height:14.4px;text-align:justify}
.nachos-desc b{font-weight:800}
.pack{position:absolute;left:792px;width:158px}
.pack .item__row{font-size:11px}
.pack .price-w{color:var(--yellow)}
</style>
</head>
<body>
<div class="board">

  <span class="ornament" style="left:53px;top:37px" role="img" aria-label="Hand-drawn star ornament"></span>
  <span class="ornament" style="left:1117px;top:37px" role="img" aria-label="Hand-drawn star ornament"></span>
  <span class="ornament" style="left:53px;top:550px" role="img" aria-label="Hand-drawn star ornament"></span>
  <span class="ornament" style="left:1117px;top:550px" role="img" aria-label="Hand-drawn star ornament"></span>

  <!-- Beef burgers -->
  <div class="band" style="left:120px;top:34px;width:208px;height:32px;font-size:30px">BEEF BURGERS</div>
  <p class="intro abs" style="left:66px;top:70px;width:320px">All our patties are 100% natural beef. We know because we grind it ourselves, smashed to order on a hot grill rite in from of you</p>
  <p class="note abs" style="left:66px;top:122px;width:320px">DOUBLE PATTY ADD 4</p>

  <div class="item" style="left:67px;top:141px">
    <div class="item__row"><span>CLASSIC BEEF</span><span class="item__dots"></span><span>8.9</span></div>
    <p class="item__desc">Shredded lettuce, sliced tomato, caramelised onions, beetroot and BBQ sauce on a buttered sesame seed bum.</p>
  </div>
  <div class="item" style="left:67px;top:193px">
    <div class="item__row"><span>CHEESE BURGER</span><span class="item__dots"></span><span>9.5</span></div>
    <p class="item__desc">Dill pickles, minced onion, american cheese, mustard and ketchup on soft milk bun.</p>
  </div>
  <div class="item" style="left:67px;top:240px">
    <div class="item__row"><span>FLAME GRILL</span><span class="item__dots"></span><span>9.5</span></div>
    <p class="item__desc">Shredded lettuce, sliced tomato, minced onion, dill pickles, american cheese, mayo and ketchup on a soft bun.</p>
  </div>
  <div class="item" style="left:67px;top:289px">
    <div class="item__row"><span>BIG DOCK</span><span class="item__dots"></span><span>9.9</span></div>
    <p class="item__desc">Shredded lettuce, dil pickles, minced onion, american cheese and special sauce on a soft milk bun.</p>
  </div>

  <!-- Brand -->
  <div class="brand">
    <div class="brand__name">Harbor<br>Burger</div>
    <div class="brand__tag">CLASSICS FOR A REASON</div>
  </div>

  <!-- Chicken burgers -->
  <div class="band" style="left:815px;top:34px;width:268px;height:32px;font-size:30px">CHICKEN BURGERS</div>
  <p class="intro abs" style="left:806px;top:70px;width:320px">All our patties are 100% natural beef. We know because we grind it ourselves, smashed to order on a hot grill rite in from of you</p>
  <p class="note abs" style="left:806px;top:121px;width:320px">DOUBLE PATTY ADD 4</p>

  <div class="item" style="left:811px;top:140px">
    <div class="item__row"><span>CLASSIC BEEF</span><span class="item__dots"></span><span>8.9</span></div>
    <p class="item__desc">Shredded lettuce, sliced tomato, caramelised onions, beetroot and BBQ sauce on a buttered sesame seed bum.</p>
  </div>
  <div class="item" style="left:811px;top:192px">
    <div class="item__row"><span>CHEESE BURGER</span><span class="item__dots"></span><span>9.5</span></div>
    <p class="item__desc">Dill pickles, minced onion, american cheese, mustard and ketchup on soft milk bun.</p>
  </div>
  <div class="item" style="left:811px;top:239px">
    <div class="item__row"><span>FLAME GRILL</span><span class="item__dots"></span><span>9.5</span></div>
    <p class="item__desc">Shredded lettuce, sliced tomato, minced onion, dill pickles, american cheese, mayo and ketchup on a soft bun.</p>
  </div>
  <div class="item" style="left:811px;top:287px">
    <div class="item__row"><span>TRUFFLED</span><span class="item__dots"></span><span>9.9</span></div>
    <p class="item__desc">Rocket, caramelised onion, dill pickles, havarti cheese and truffle infused mayo on a soft milk bun.</p>
  </div>

  <div class="rule" style="left:53px;top:350px;width:418px"></div>
  <div class="rule" style="left:716px;top:350px;width:427px"></div>

  <!-- Sides -->
  <div class="band" style="left:527px;top:338px;width:135px;height:37px;font-size:34px">SIDES</div>
  <div class="sides" style="top:394px">
    <div class="item__row"><span>FRIES</span><span class="item__dots"></span><span>3.5</span></div>
    <div class="item__row" style="margin-top:2px"><span>CRISPY TENDERS</span><span class="item__dots"></span><span>6.9</span></div>
    <p class="sides__desc" style="margin-top:17px">Breaded and fried chicken tenders with secret seasoning. <b>(2 PCS).</b></p>
  </div>
  <div class="art" style="left:495px;top:498px;width:109px;height:62px" role="img" aria-label="Line sketch of a burger"></div>
  <div class="art" style="left:628px;top:474px;width:52px;height:88px" role="img" aria-label="Line sketch of a drink glass with ice"></div>

  <!-- Nachos & loaded fries -->
  <div class="band band--red" style="left:118px;top:363px;width:228px;height:34px;font-size:25px">NACHOS &amp; LOADED FRIES</div>
  <div class="band" style="left:116px;top:422px;width:74px;height:18px;font-size:14px">STEP ONE</div>
  <div class="band" style="left:291px;top:422px;width:74px;height:18px;font-size:14px">STEP TWO</div>
  <p class="step-label abs" style="left:90px;top:453px;width:120px">CHOOSE EITHER,</p>
  <p class="step-label abs" style="left:272px;top:452px;width:120px">CHOOSE ONE,</p>

  <div class="choice abs" style="left:61px;top:482px;width:180px">
    <div class="item__row" style="color:var(--white);font-size:11px"><span>SEASONED FRIES</span><span class="item__dots"></span><span class="price-w">9.9</span></div>
    <p style="margin-top:14px">OR FRESHLY COOKED</p>
    <div class="item__row" style="color:var(--white);font-size:11px"><span>CORN CHIPS</span><span class="item__dots"></span><span class="price-w">11.5</span></div>
  </div>
  <p class="nachos-desc abs" style="left:251px;top:480px;width:163px"><b>GUACAMOLE</b> salsa fresca, guacamole, jalapeñoz, cheese sauce and sour cream. <b>BEEF CHILLI</b> salsa fresca, beef chilli, jalapeños, cheese sauce and sour cream.</p>

  <!-- Buffalo chicken ribs -->
  <div class="band band--red" style="left:833px;top:368px;width:227px;height:29px;font-size:23px">BUFFALO CHICKEN RIBS</div>
  <p class="intro abs" style="left:782px;top:414px;width:340px;font-size:10.3px;line-height:13.5px">Buffalo style fried chicken ribs smothered in one dur mouth-watering sauce. Served with a side of ranch sauce.</p>
  <div class="pack" style="top:469px"><div class="item__row"><span>6 PACK</span><span class="item__dots"></span><span class="price-w">6.9</span></div></div>
  <div class="pack" style="top:497px"><div class="item__row"><span>12 PACK</span><span class="item__dots"></span><span class="price-w">12.9</span></div></div>
  <div class="pack" style="top:526px"><div class="item__row"><span>24 PACK</span><span class="item__dots"></span><span class="price-w">23.9</span></div></div>
  <p class="abs" style="left:986px;top:484px;font-size:11px;line-height:14.5px;font-weight:700;color:var(--yellow)">CLASSIC HOT SAUCE<br>OR SMOKY BBQ</p>

</div>
</body>
</html>
```